TORNWICK Pizza Flyer / Menu

Hello so its a new pizza shop called Tornwick. I need a flyer menu designed . it will be 30cm tall and 10.5cm wide. i made one which i have uploaded but as you can see im not very skillfull design wise. I did want the logo on the front with the photo of the counter in the middle and then half the pizza at the bottom. then on the back i wanted all the different toppings ( doesnt have to be the same pics as i have used ) and then drinks and desserts underneath and our contact details. I dont want to include our signature specials. Also facebook/twitter and instagram logos somewhere. the font i have been using is called 'AR CENA' i have attached a rough sketch i have put together to give you an idea too. thanks

Industry/Entity Type

Shop

```html
<!DOCTYPE html>
<html lang="en">
<head>
<meta charset="utf-8">
<title>Tornwick Pizza Flyer</title>
<link rel="stylesheet" href="https://fonts.googleapis.com/css2?family=Kalam:wght@400;700&family=Abril+Fatface&family=Luckiest+Guy&display=swap">
<style>
  :root {
    --black: #000000;
    --white: #ffffff;
    --orange: #ef9a0e;
    --yellow: #f7e640;
    --ink: #111111;
    --pink-light: #f7b6a3;
    --pink-mid: #f19a86;
    --pink-deep: #e87a74;
    --board: #efe6d8;
  }
  * { box-sizing: border-box; margin: 0; padding: 0; }
  html, body { width: 1200px; height: 1115px; overflow: hidden; background: var(--black); }
  body { position: relative; font-family: "Kalam", cursive; color: var(--ink); }

  .panel { position: absolute; top: 106px; width: 316px; height: 904px; overflow: hidden; border: 1px solid var(--orange); }
  .panel--front { left: 274px; background: var(--white); }
  .panel--back { left: 629px; background: linear-gradient(160deg, var(--pink-light) 0%, var(--pink-mid) 45%, var(--pink-deep) 100%); }

  /* Front */
  .photo-counter { position: absolute; left: 0; top: 0; width: 316px; height: 590px;
    background: linear-gradient(170deg, #d8d2cc 0%, #a7a29d 18%, #8a6a4a 32%, #b8483a 45%, #6d7a3a 58%, #b9b4ae 100%); }
  .photo-pizza { position: absolute; left: 0; top: 590px; width: 316px; height: 220px;
    background: linear-gradient(180deg, #3e3a2c 0%, #9c6b34 35%, #c9873d 60%, #2a1a14 100%); }
  .front-badge { position: absolute; left: -21px; top: 286px; width: 358px; height: 358px; border-radius: 50%; background: var(--white); }
  .front-logo { position: absolute; left: 0; top: 352px; width: 316px; text-align: center; }
  .logo-tag { font-weight: 700; font-size: 22px; letter-spacing: 2px; line-height: 1; }
  .logo-dot { display: block; width: 126px; height: 126px; border-radius: 50%; background: var(--orange); margin: 8px auto 8px; }
  .logo-name { font-weight: 700; font-size: 46px; letter-spacing: 2px; line-height: 1; }
  .front-band { position: absolute; left: 0; bottom: 0; width: 316px; height: 95px; background: var(--orange);
    display: flex; align-items: center; justify-content: center; color: var(--white); font-weight: 700; font-size: 23px; letter-spacing: 0.5px; }

  /* Back */
  .back-badge { position: absolute; left: 154px; top: 10px; width: 150px; height: 150px; border-radius: 50%; background: var(--white); text-align: center; padding-top: 26px; }
  .back-badge .logo-tag { font-size: 11px; letter-spacing: 1px; }
  .back-badge .logo-dot { width: 54px; height: 54px; margin: 4px auto 3px; }
  .back-badge .logo-name { font-size: 19px; letter-spacing: 1px; }

  .price-disc { position: absolute; left: 80px; top: 136px; width: 62px; height: 62px; border-radius: 50%; background: var(--black);
    color: var(--white); font-family: "Abril Fatface", serif; font-size: 18px; display: flex; align-items: center; justify-content: center; padding-bottom: 10px; }
  .build-title { position: absolute; left: 26px; top: 168px; font-family: "Abril Fatface", serif; font-size: 28px; color: var(--white); line-height: 1; z-index: 2; }

  .toppings { position: absolute; left: 27px; top: 201px; width: 263px; height: 158px; background: var(--board);
    box-shadow: 0 2px 4px rgba(0,0,0,.3); display: grid; grid-template-columns: repeat(7, 1fr); grid-template-rows: repeat(4, 1fr); padding: 6px 5px 4px; gap: 2px 3px; }
  .topping { display: flex; flex-direction: column; align-items: center; }
  .topping-pic { width: 28px; height: 26px; border: 1px solid #999; }
  .topping-name { font-family: Arial, sans-serif; font-size: 3.6px; font-weight: 700; margin-top: 2px; text-transform: uppercase; white-space: nowrap; }

  .section-title { position: absolute; left: 45px; font-weight: 700; font-size: 22px; color: var(--white); opacity: .85; letter-spacing: 0.5px; line-height: 1; }
  .item { position: absolute; z-index: 2; font-size: 12px; line-height: 1.05; text-transform: uppercase; font-weight: 400; white-space: nowrap; }
  .item small { display: block; font-size: 7px; }
  .price { position: absolute; z-index: 1; width: 34px; height: 34px; border-radius: 50%; background: var(--white);
    color: var(--orange); font-family: "Abril Fatface", serif; font-size: 11px; display: flex; align-items: flex-start; justify-content: center; padding-top: 6px; }
  .divider { position: absolute; left: 17px; top: 494px; width: 283px; height: 2px; background: var(--ink); }

  .delivery { position: absolute; left: 24px; top: 618px; width: 262px; height: 72px; background: var(--orange);
    text-align: center; color: var(--white); padding-top: 10px; }
  .delivery p { font-size: 13px; line-height: 1.15; letter-spacing: 1.2px; text-transform: uppercase; }
  .delivery .minimum { font-family: "Abril Fatface", serif; color: var(--yellow); font-size: 17px; letter-spacing: .5px; text-transform: none; margin-top: 2px; }

  .phone { position: absolute; left: 0; top: 700px; width: 316px; text-align: center; font-weight: 700; font-size: 34px; letter-spacing: 1px; }
  .follow { position: absolute; left: -40px; top: 744px; width: 396px; height: 320px; border-radius: 50% 50% 0 0 / 45% 45% 0 0; background: var(--white); }
  .follow-text { position: absolute; left: 0; top: 784px; width: 316px; text-align: center; font-family: Arial, sans-serif; font-size: 12px; line-height: 1.15; }
  .free { position: absolute; left: 0; top: 812px; width: 316px; text-align: center; font-family: "Luckiest Guy", "Kalam", cursive; font-weight: 700; font-size: 25px; line-height: 1.2; color: var(--orange); }
  .social { position: absolute; left: 87px; top: 850px; display: flex; gap: 14px; }
  .social-box { width: 38px; height: 38px; border-radius: 5px; background: #4e6a9a; }
</style>
</head>
<body>

<section class="panel panel--front">
  <div class="photo-counter" role="img" aria-label="Photo of the pizza counter with trays of fresh toppings"></div>
  <div class="photo-pizza" role="img" aria-label="Photo of freshly baked pizza slices"></div>
  <div class="front-badge"></div>
  <div class="front-logo">
    <div class="logo-tag">DESIGNER PIZZA</div>
    <span class="logo-dot"></span>
    <div class="logo-name">TORNWICK</div>
  </div>
  <div class="front-band">QUICK - KUSTOM - PIZZA</div>
</section>

<section class="panel panel--back">
  <div class="back-badge">
    <div class="logo-tag">DESIGNER PIZZA</div>
    <span class="logo-dot"></span>
    <div class="logo-name">TORNWICK</div>
  </div>

  <div class="price-disc">£6.99</div>
  <div class="build-title">Build It!</div>

  <div class="toppings">
    <div class="topping"><div class="topping-pic" role="img" aria-label="Pineapple" style="background:#e8d24a"></div><span class="topping-name">Pineapple</span></div>
    <div class="topping"><div class="topping-pic" role="img" aria-label="Pepperoni" style="background:#e0743a"></div><span class="topping-name">Pepperoni</span></div>
    <div class="topping"><div class="topping-pic" role="img" aria-label="Red pepper" style="background:#d0201c"></div><span class="topping-name">Red pepper</span></div>
    <div class="topping"><div class="topping-pic" role="img" aria-label="Black olive" style="background:#1b1b22"></div><span class="topping-name">Black olive</span></div>
    <div class="topping"><div class="topping-pic" role="img" aria-label="Spinach" style="background:#3f7a2c"></div><span class="topping-name">Spinach</span></div>
    <div class="topping"><div class="topping-pic" role="img" aria-label="Garlic" style="background:#c9c4b4"></div><span class="topping-name">Garlic</span></div>
    <div class="topping"><div class="topping-pic" role="img" aria-label="Mozzarella" style="background:#ead8a0"></div><span class="topping-name">Mozzarella</span></div>
    <div class="topping"><div class="topping-pic" role="img" aria-label="Green olive" style="background:#b9c43a"></div><span class="topping-name">Green olive</span></div>
    <div class="topping"><div class="topping-pic" role="img" aria-label="Ricotta" style="background:#b8bcc0"></div><span class="topping-name">Ricotta</span></div>
    <div class="topping"><div class="topping-pic" role="img" aria-label="Green pepper" style="background:#3e9a2a"></div><span class="topping-name">Green pepper</span></div>
    <div class="topping"><div class="topping-pic" role="img" aria-label="Onion" style="background:#7a2e5a"></div><span class="topping-name">Onion</span></div>
    <div class="topping"><div class="topping-pic" role="img" aria-label="Cheddar cheese" style="background:#e4a23a"></div><span class="topping-name">Cheddar</span></div>
    <div class="topping"><div class="topping-pic" role="img" aria-label="Basil" style="background:#2f8a2a"></div><span class="topping-name">Basil</span></div>
    <div class="topping"><div class="topping-pic" role="img" aria-label="Pulled chicken" style="background:#b88a5a"></div><span class="topping-name">Pulled chicken</span></div>
    <div class="topping"><div class="topping-pic" role="img" aria-label="Pulled beef" style="background:#7a4a34"></div><span class="topping-name">Pulled beef</span></div>
    <div class="topping"><div class="topping-pic" role="img" aria-label="Mushroom" style="background:#a89a84"></div><span class="topping-name">Mushroom</span></div>
    <div class="topping"><div class="topping-pic" role="img" aria-label="Tomato" style="background:#e2401e"></div><span class="topping-name">Tomato</span></div>
    <div class="topping"><div class="topping-pic" role="img" aria-label="Salami" style="background:#b0604e"></div><span class="topping-name">Salami</span></div>
    <div class="topping"><div class="topping-pic" role="img" aria-label="Capers" style="background:#8aa23a"></div><span class="topping-name">Capers</span></div>
    <div class="topping"><div class="topping-pic" role="img" aria-label="Anchovies" style="background:#9a7a58"></div><span class="topping-name">Anchovies</span></div>
    <div class="topping"><div class="topping-pic" role="img" aria-label="Jalapenos" style="background:#4a8a2a"></div><span class="topping-name">Jalapenos</span></div>
    <div class="topping"><div class="topping-pic" role="img" aria-label="Corn" style="background:#e6b21e"></div><span class="topping-name">Corn</span></div>
    <div class="topping"><div class="topping-pic" role="img" aria-label="Chilli" style="background:#b81e1e"></div><span class="topping-name">Chilli</span></div>
    <div class="topping"><div class="topping-pic" role="img" aria-label="BBQ sauce" style="background:#4a1a12"></div><span class="topping-name">B-B-Q</span></div>
    <div class="topping"><div class="topping-pic" role="img" aria-label="Pesto" style="background:#4a9a34"></div><span class="topping-name">Pesto</span></div>
    <div class="topping"><div class="topping-pic" role="img" aria-label="Chorizo" style="background:#8a3a2a"></div><span class="topping-name">Chorizo</span></div>
    <div class="topping"><div class="topping-pic" role="img" aria-label="Parmesan" style="background:#eadcb0"></div><span class="topping-name">Parmesan</span></div>
    <div class="topping"><div class="topping-pic" role="img" aria-label="Sweet chilli" style="background:#e0301e"></div><span class="topping-name">Sweet chilli</span></div>
  </div>

  <div class="section-title" style="top:378px;">DESSERTS...</div>
  <div class="item" style="left:45px; top:411px; font-size:11px;">Bannahazella<br>Pizza !!!<small>(LEGENDARY)</small></div>
  <div class="price" style="left:100px; top:419px;">£3.99</div>
  <div class="price" style="left:162px; top:388px;">£2.49</div>
  <div class="item" style="left:198px; top:400px;">Choco<br>Dream cake</div>
  <div class="price" style="left:146px; top:435px;">£2.49</div>
  <div class="item" style="left:126px; top:456px; text-align:center;">Creme<br>Brulee</div>
  <div class="price" style="left:210px; top:431px;">£2.49</div>
  <div class="item" style="left:222px; top:455px;">Tiramisu</div>

  <div class="divider"></div>

  <div class="section-title" style="top:516px;">DRINKS...</div>
  <div class="price" style="left:122px; top:521px;">£0.99</div>
  <div class="item" style="left:58px; top:546px;">Blood orange</div>
  <div class="price" style="left:190px; top:521px;">£0.99</div>
  <div class="item" style="left:201px; top:546px;">Lemon</div>
  <div class="item" style="left:90px; top:573px;">Orangeade</div>
  <div class="price" style="left:144px; top:572px; padding-top:16px;">£0.99</div>
  <div class="item" style="left:226px; top:573px;">Fizzy cola</div>
  <div class="price" style="left:224px; top:574px; padding-top:16px;">£0.89</div>

  <div class="delivery">
    <p>Wood stone pizza delivered<br>hot to your door step</p>
    <p class="minimum">Minimum Order £12</p>
  </div>

  <div class="phone">0208 555 0147</div>

  <div class="follow"></div>
  <p class="follow-text">FOLLOW US FOR UPDATES,<br>OFFERS AND IF YOU LUCKY...</p>
  <div class="free">A FREE PIZZA</div>
  <div class="social" aria-label="Social media links">
    <span class="social-box" aria-label="Social profile one"></span>
    <span class="social-box" style="background:#4aa8e0" aria-label="Social profile two"></span>
    <span class="social-box" style="background:#6d7c90" aria-label="Social profile three"></span>
  </div>
</section>

</body>
</html>
```